A Hair, Beauty and Nails Wholesalers Needs a Business Card Design

We need a business card design for our company which is being passed from parents to daughter, so we wont to re-launch the company with an updated, modern, sophisticated, elegant, chic and fresh look which still incorporates the original colour scheme of Hot Pink, Dark Grey and White. The original logo which is attached can be used on the card but we would like to see some designs with the logo and some without, as we have not yet decided if we want the logo on the card. The name of our company is 'RM's Distributors' and the name of our website is RM's GlowandPolish.example.au. We specialise in supplying a massive range of Hair, Beauty and Nail products to the industry. We are based in QLD, Australia but ship many orders via our website all across Australia.

Industry/Entity Type

Business

```html
<!DOCTYPE html>
<html lang="en">
<head>
<meta charset="utf-8">
<title>RM's Distributors – Business Card</title>
<link href="https://fonts.googleapis.com/css2?family=Fira+Sans+Condensed:wght@400;500&family=Noto+Serif:wght@400&display=swap" rel="stylesheet">
<style>
  :root {
    --hot-pink: #d6178f;
    --card-grey: #5b5b5d;
    --ink-dark: #2f2f31;
    --ink-light: #e4e4e7;
    --white: #f4f4f6;
    --backdrop: #dcdcde;
  }
  * { margin: 0; padding: 0; box-sizing: border-box; }
  html, body { width: 1200px; height: 1000px; overflow: hidden; }
  body {
    background: var(--backdrop);
    display: flex;
    flex-direction: column;
    align-items: center;
    justify-content: center;
    gap: 56px;
    font-family: "Fira Sans Condensed", Arial, sans-serif;
  }
  .card {
    position: relative;
    width: 700px;
    height: 428px;
    overflow: hidden;
    box-shadow: 0 6px 18px rgba(0,0,0,.18);
  }

  /* Front */
  .card-front { background: var(--card-grey); }
  .brand-mark {
    position: absolute;
    left: 70px;
    top: 50%;
    transform: translateY(-50%);
    display: flex;
    align-items: center;
    gap: 20px;
  }
  .brand-dot {
    width: 56px; height: 56px;
    border-radius: 50%;
    background: var(--hot-pink);
    flex: none;
  }
  .brand-name {
    font-size: 54px;
    font-weight: 400;
    color: var(--ink-light);
    letter-spacing: 1px;
    white-space: nowrap;
  }
  .front-web {
    position: absolute;
    right: 16px;
    top: 50%;
    transform: translateY(-50%);
    writing-mode: vertical-rl;
    font-family: "Noto Serif", Georgia, serif;
    font-size: 20px;
    letter-spacing: 2px;
    color: var(--white);
    white-space: nowrap;
  }

  /* Back */
  .card-back { display: flex; flex-direction: column; }
  .band-address,
  .band-contact {
    background: var(--hot-pink);
    color: var(--ink-dark);
    font-size: 22px;
    line-height: 1.35;
    padding: 0 34px;
    display: flex;
    align-items: center;
  }
  .band-address { height: 140px; }
  .band-identity {
    height: 150px;
    background: var(--card-grey);
    display: flex;
    justify-content: space-between;
    align-items: center;
    padding: 0 34px;
  }
  .back-brand {
    font-size: 24px;
    color: var(--ink-light);
    white-space: nowrap;
  }
  .person { text-align: center; }
  .person-name {
    font-size: 40px;
    font-weight: 500;
    color: var(--ink-light);
    letter-spacing: .5px;
  }
  .person-role {
    font-size: 22px;
    color: var(--ink-light);
    margin-top: 2px;
  }
  .band-contact {
    flex: 1;
    justify-content: space-between;
  }
</style>
</head>
<body>

  <section class="card card-front" aria-label="Card front">
    <div class="brand-mark">
      <span class="brand-dot"></span>
      <span class="brand-name">RM's glowandpolish</span>
    </div>
    <p class="front-web">www.glowandpolish.example.au</p>
  </section>

  <section class="card card-back" aria-label="Card back">
    <div class="band-address">
      <p class="contact-address">RM's Distributors<br>58 Harbour Lane<br>Springvale, QLD, 4000</p>
    </div>
    <div class="band-identity">
      <p class="back-brand">RM's glowandpolish</p>
      <div class="person">
        <p class="person-name">Danielle Morrow</p>
        <p class="person-role">Manager</p>
      </div>
    </div>
    <div class="band-contact">
      <p class="contact-phone">(07) 5550 0182</p>
      <p class="contact-email">admin@glowandpolish.example.au</p>
    </div>
  </section>

</body>
</html>
```